Business Card Design needed for start up company Pramora

In need of a new business card designed for a start up company based in Sydney, Pramora is a new start up innovative Company, our mission it to make property accessible for everyday Australian and to become the leading Real Estate platform in Australia. We want it to be fresh and clean.

Industry/Entity Type

Financial

Contact Information for Business Card

Section for Name
Section for Title

PRAMORA - Where Doors Open Wide
Mobile:
Direct:

Font styles to use
Sans Serif

Colors
33a6d7
0692cd
0255a3
ffffff

Requirements
Must have
• Logo, all business card details

```html
<!DOCTYPE html>
<html lang="en">
<head>
<meta charset="utf-8">
<title>Pramora Business Card</title>
<link rel="stylesheet" href="https://fonts.googleapis.com/css2?family=Source+Sans+3:wght@400;800&display=swap">
<style>
  :root {
    --backdrop: #e1e7e6;
    --paper: #ffffff;
    --royal-blue: #0b47f4;
    --edge-blue: #0455e0;
    --sky-blue: #39b3f3;
    --rule-blue: #a6e0f7;
    --navy: #1a3aa6;
  }
  * { margin: 0; padding: 0; box-sizing: border-box; }
  html, body { width: 1200px; height: 1200px; overflow: hidden; }
  body {
    background: var(--backdrop);
    position: relative;
    font-family: "Source Sans 3", sans-serif;
  }
  .card { position: absolute; overflow: hidden; }

  /* Front side */
  .card-front { left: 212px; top: 90px; width: 786px; height: 435px; background: var(--paper); }
  .card-front .chevron { position: absolute; left: 0; top: 0; }
  .brand { position: absolute; display: flex; align-items: center; }
  .brand-dot { border-radius: 50%; background: var(--sky-blue); flex: none; }
  .brand-name { font-weight: 800; color: var(--navy); letter-spacing: -0.5px; line-height: 1; white-space: nowrap; }
  .card-front .brand { left: 61px; top: 157px; gap: 10px; }
  .card-front .brand-dot { width: 70px; height: 70px; }
  .card-front .brand-name { font-size: 42px; }

  /* Back side */
  .card-back { left: 216px; top: 633px; width: 783px; height: 457px; background: var(--sky-blue); }
  .back-top { position: absolute; left: 0; top: 0; width: 100%; height: 265px; background: var(--royal-blue); border-bottom: 3px solid var(--rule-blue); }
  .card-back .brand { left: 39px; top: 32px; gap: 5px; }
  .card-back .brand-dot { width: 40px; height: 40px; }
  .card-back .brand-name { font-size: 23px; }
  .holder-name {
    position: absolute; left: 259px; top: 104px; width: 366px;
    font-size: 48px; color: var(--sky-blue); line-height: 1.1;
    border-bottom: 2px solid var(--sky-blue); padding-bottom: 2px;
    white-space: nowrap;
  }
  .holder-title {
    position: absolute; left: 286px; top: 171px;
    font-size: 31px; color: var(--paper); letter-spacing: 3.2px; line-height: 1.2;
    white-space: nowrap;
  }
  .contact {
    position: absolute; left: 258px; top: 336px;
    font-size: 23px; color: var(--paper); letter-spacing: 1.2px; line-height: 29.5px;
    white-space: nowrap;
  }
</style>
</head>
<body>
  <section class="card card-front" aria-label="Card front">
    <svg class="chevron" width="786" height="435" viewBox="0 0 786 435">
      <polygon points="483,0 505,0 375,218 505,435 483,435 353,218" fill="var(--sky-blue)"/>
      <polygon points="505,0 786,0 786,435 505,435 375,218" fill="var(--royal-blue)"/>
      <rect x="748" y="0" width="38" height="435" fill="var(--edge-blue)"/>
    </svg>
    <div class="brand">
      <span class="brand-dot"></span>
      <span class="brand-name">PRAMORA</span>
    </div>
  </section>

  <section class="card card-back" aria-label="Card back">
    <div class="back-top"></div>
    <div class="brand">
      <span class="brand-dot"></span>
      <span class="brand-name">PRAMORA</span>
    </div>
    <p class="holder-name">Section for Name</p>
    <p class="holder-title">&lt; Section for Title &gt;</p>
    <div class="contact">
      <p>PRAMORA - Where Doors Open Wide</p>
      <p>Mobile:</p>
      <p>Direct:</p>
    </div>
  </section>
</body>
</html>
```